Building company business card

Design and print business cards for BREVOTA PTY LTD.
A residantial homes building company.
Pixel Forge already designed the company Logo.

```html
<!DOCTYPE html>
<html lang="en">
<head>
<meta charset="utf-8">
<title>BREVOTA PTY LTD – Business Card</title>
<link rel="stylesheet" href="https://fonts.googleapis.com/css2?family=Roboto:wght@400;500;700&family=Roboto+Condensed:wght@700&display=swap">
<style>
  :root {
    --navy: #1b2a78;
    --gold-light: #e6bd5e;
    --gold: #d3a23f;
    --gold-dark: #b8832a;
    --ink: #1d1d1d;
    --paper: #ffffff;
    --backdrop: #c4c4c4;
  }
  * { box-sizing: border-box; margin: 0; padding: 0; }
  html, body { width: 1200px; height: 800px; overflow: hidden; }
  body {
    background: var(--backdrop);
    font-family: "Roboto", Arial, sans-serif;
    color: var(--ink);
    position: relative;
  }
  .card {
    position: absolute;
    top: 235px;
    width: 540px;
    height: 330px;
    box-shadow: 0 10px 28px rgba(0,0,0,.28);
    overflow: hidden;
  }
  .card--front { left: 40px; background: var(--paper); }
  .card--back {
    left: 620px;
    background: linear-gradient(160deg, var(--gold-light) 0%, var(--gold) 50%, var(--gold-dark) 100%);
  }
  .brand-block {
    position: absolute;
    left: 0; top: 0;
    width: 250px; height: 282px;
    display: flex; align-items: center; justify-content: center; gap: 10px;
  }
  .brand-mark { width: 18px; height: 18px; background: var(--gold); }
  .brand-name {
    font-family: "Roboto", Arial, sans-serif;
    font-weight: 700;
    font-size: 40px;
    color: var(--navy);
    letter-spacing: 1px;
  }
  .divider {
    position: absolute;
    left: 250px; top: 18px;
    width: 2px; height: 250px;
    background: linear-gradient(to bottom, rgba(0,0,0,0), rgba(0,0,0,.18) 30%, rgba(0,0,0,.18) 70%, rgba(0,0,0,0));
  }
  .details { position: absolute; left: 276px; top: 34px; right: 16px; }
  .person-name {
    font-family: "Roboto Condensed", Arial Narrow, sans-serif;
    font-weight: 700;
    font-size: 23px;
    color: var(--navy);
    line-height: 1.05;
  }
  .person-role { font-size: 15px; margin-top: 2px; }
  .contact-list { list-style: none; margin-top: 14px; }
  .contact-list li {
    display: flex; align-items: center; gap: 8px;
    font-size: 14.5px; line-height: 21px;
  }
  .contact-list svg { width: 13px; height: 13px; flex: none; fill: var(--navy); }
  .company { margin-top: 12px; font-size: 14.5px; line-height: 20px; }
  .company-name { font-weight: 700; color: var(--navy); }
  .registration-band {
    position: absolute;
    left: 0; right: 0; bottom: 0;
    height: 48px;
    background: linear-gradient(90deg, var(--gold-light), var(--gold) 60%, var(--gold-dark));
    color: #fff;
    font-size: 14px;
    letter-spacing: .5px;
    display: flex; align-items: center; justify-content: center;
  }
  .back-pattern { position: absolute; inset: 0; }
  .back-name {
    position: absolute;
    right: 48px; bottom: 100px;
    font-weight: 700;
    font-size: 16px;
    color: #fff;
    letter-spacing: 1px;
  }
</style>
</head>
<body>
  <section class="card card--front" aria-label="Business card front">
    <div class="brand-block">
      <span class="brand-mark" aria-hidden="true"></span>
      <span class="brand-name">BREVOTA</span>
    </div>
    <div class="divider" aria-hidden="true"></div>
    <div class="details">
      <h1 class="person-name">DAMIAN (Dan) KORRES</h1>
      <p class="person-role">Director</p>
      <ul class="contact-list">
        <li>
          <svg viewBox="0 0 16 16" aria-hidden="true"><path d="M3.6 1.5l2.3 2.6-1.3 1.8c.9 2 2.5 3.6 4.5 4.5l1.8-1.3 2.6 2.3-1.4 2.1C7 13.3 2.7 9 2 3l1.6-1.5z"/></svg>
          <span>0400 318 527</span>
        </li>
        <li>
          <svg viewBox="0 0 16 16" aria-hidden="true"><path d="M4 1h8v14H4V1zm1.5 1.5v9h5v-9h-5zM7 12.5v1h2v-1H7z"/></svg>
          <span>0400 642 190</span>
        </li>
        <li>
          <svg viewBox="0 0 16 16" aria-hidden="true"><path d="M1 3h14v10H1V3zm1.5 1.2v.3L8 8.6l5.5-4.1v-.3h-11z"/></svg>
          <span>dk@brevota-pl.com</span>
        </li>
        <li>
          <svg viewBox="0 0 16 16" aria-hidden="true"><path d="M8 1a7 7 0 100 14A7 7 0 008 1zm-5.4 6.3h2.3c.1-1.6.5-3 1.1-4A5.6 5.6 0 002.6 7.3zm0 1.4a5.6 5.6 0 003.4 4c-.6-1-1-2.4-1.1-4H2.6zm3.7 0c.1 2 .9 3.6 1.7 4.3.8-.7 1.6-2.3 1.7-4.3H6.3zm0-1.4h3.4C9.6 5.3 8.8 3.7 8 3c-.8.7-1.6 2.3-1.7 4.3zm4.8 1.4c-.1 1.6-.5 3-1.1 4a5.6 5.6 0 003.4-4h-2.3zm2.3-1.4a5.6 5.6 0 00-3.4-4c.6 1 1 2.4 1.1 4h2.3z"/></svg>
          <span>www.brevota-pl.com</span>
        </li>
      </ul>
      <div class="company">
        <p class="company-name">BREVOTA PTY LTD</p>
        <p>PO Box 482</p>
        <p>Northvale Vic 3999</p>
      </div>
    </div>
    <footer class="registration-band">ABN- 24 816 502 947 &nbsp;|&nbsp; CDB-U 58104</footer>
  </section>

  <section class="card card--back" aria-label="Business card back">
    <div class="back-pattern" role="img" aria-label="Embossed repeating brand pattern on gold foil"></div>
    <span class="back-name">BREVOTA</span>
  </section>
</body>
</html>
```